Design professional label for greener chemicals (cleaning and lubrication) brand

Design a b2b professional label that is based on the examples given.
Size: 135 x 200 mm, please use text of the label description doc (only the kalmir stainless steel polish example design document has the right text and size)
It should include:
1. Logo, can be fully changed except the shape of "KALMIR", colors and fonts of the rest can be customized
2. Focus should be on professional market, we would like to express the professionalism and high quality of the product
3. Focus should be on our brand name "KALMIR CLEANER COMPOUNDS"
4. Should include product name, product description, danger sentences, danger symbol, user instructions, image
5. Should include numbers that explain what the product does: 1. Prewash 2. Clean 3. Protect 4. Preserve and highlight number 2.

Target Market(s)

Professional cleaning companies, steel industry, food industry, pharmacy industry

Industry/Entity Type

Cleaning industry, steel industry, food industry, boat cleaning, car cleaning, professional lubrication

Font styles to use
Sans Serif

Requirements
Must have
• Professional look, clean look, image, focus on our brand name
Nice to have
• Numbers (see explanation), label divided in three parts (logo and product name and image in the middle as the highlight)

```html
<!DOCTYPE html>
<html lang="en">
<head>
<meta charset="utf-8">
<title>Kalmir Stainless Steel Polish Label</title>
<link rel="stylesheet" href="https://fonts.googleapis.com/css2?family=Montserrat:wght@500;600;700;800;900&family=Oswald:wght@700&display=swap">
<style>
  :root {
    --backdrop: #8f8e90;
    --label-bg: #ececec;
    --ink: #121212;
    --brand-green: #4fb51e;
    --silver: #b9b9bb;
    --step-box: #bdbdbd;
    --hazard-red: #d7261e;
    --steel-light: #e4e6e8;
    --steel-dark: #9a9ea3;
    --white: #ffffff;
  }
  * { box-sizing: border-box; margin: 0; padding: 0; }
  html, body {
    width: 1200px; height: 946px; overflow: hidden;
    background: var(--backdrop);
  }
  .label {
    position: absolute; left: 290px; top: 43px;
    width: 620px; height: 860px;
    background: var(--label-bg);
    font-family: "Montserrat", sans-serif;
    color: var(--ink);
    overflow: hidden;
  }
  .label__header { position: absolute; left: 0; top: 0; width: 620px; height: 150px; }
  .eco-badge {
    position: absolute; top: 62px; left: 0; width: 100%;
    display: flex; justify-content: center; align-items: center; gap: 8px;
    font-weight: 800; font-size: 30px; color: var(--white); letter-spacing: 1px;
  }
  .eco-badge__dot { width: 14px; height: 14px; border-radius: 50%; background: var(--brand-green); }

  .brand { position: absolute; top: 150px; left: 0; width: 100%; text-align: center; }
  .brand__name {
    font-weight: 900; font-size: 112px; line-height: 1; letter-spacing: -3px;
    color: var(--brand-green);
  }
  .brand__tagline { margin-top: 2px; font-weight: 800; font-size: 31px; letter-spacing: 1px; }

  .product { position: absolute; top: 298px; left: 0; width: 100%; text-align: center; line-height: 1; }
  .product__main { font-family: "Oswald", sans-serif; font-weight: 700; font-size: 86px; letter-spacing: 1px; }
  .product__sub { margin-top: 2px; font-weight: 800; font-size: 44px; }

  .product-image {
    position: absolute; top: 452px; left: 32px; width: 556px; height: 92px;
    background: linear-gradient(100deg, var(--steel-dark) 0%, var(--steel-light) 45%, var(--white) 52%, var(--steel-light) 60%, var(--steel-dark) 100%);
    border: 2px solid var(--ink);
  }

  .claim { position: absolute; top: 558px; left: 32px; width: 556px; height: 34px; }
  .claim span {
    position: absolute; inset: 0; display: flex; align-items: center; justify-content: center;
    color: var(--white); font-weight: 800; font-size: 16px; letter-spacing: .5px;
  }

  .steps {
    position: absolute; top: 606px; left: 40px; width: 540px;
    display: flex; justify-content: space-between; align-items: flex-end;
  }
  .step { text-align: center; font-size: 18px; font-weight: 500; }
  .step__num {
    display: inline-block; width: 28px; height: 26px; line-height: 26px;
    background: var(--step-box); font-weight: 800; font-size: 16px; margin-bottom: 6px;
  }
  .step--highlight .step__num { background: var(--brand-green); color: var(--white); width: 34px; height: 30px; line-height: 30px; font-size: 19px; }
  .step--highlight .step__label { color: var(--brand-green); font-weight: 800; }
  .step__divider { font-size: 18px; color: var(--ink); padding-bottom: 1px; }

  .safety {
    position: absolute; top: 676px; left: 32px; width: 556px;
    display: flex; gap: 20px; font-size: 11.5px; line-height: 1.38;
  }
  .safety__block { flex: 1; display: flex; gap: 10px; }
  .safety__title { font-weight: 800; font-size: 13px; margin-bottom: 3px; letter-spacing: .5px; }
  .safety__block--hazard .safety__title { color: var(--hazard-red); }
  .hazard-symbol { flex: none; width: 52px; height: 52px; }

  .website {
    position: absolute; top: 812px; left: 0; width: 100%;
    display: flex; justify-content: center; align-items: center; gap: 10px;
    font-weight: 800; font-size: 18px;
  }
</style>
</head>
<body>
  <main class="label">
    <svg class="label__header" viewBox="0 0 620 150" aria-hidden="true">
      <path d="M0 0 H620 V36 H490 C440 36 420 135 310 135 C200 135 180 36 130 36 H0 Z" fill="var(--silver)"/>
      <path d="M0 0 H620 V26 H485 C435 26 415 122 310 122 C205 122 185 26 135 26 H0 Z" fill="var(--ink)"/>
    </svg>
    <div class="eco-badge"><span class="eco-badge__dot"></span>ECO</div>

    <section class="brand">
      <div class="brand__name">KALMIR</div>
      <div class="brand__tagline">CLEANER COMPOUNDS</div>
    </section>

    <section class="product">
      <div class="product__main">STAINLESS</div>
      <div class="product__sub">STEEL POLISH</div>
    </section>

    <div class="product-image" role="img" aria-label="Polished stainless steel surface"></div>

    <div class="claim">
      <svg viewBox="0 0 556 34" width="556" height="34" aria-hidden="true">
        <path d="M0 17 L13 0 H543 L556 17 L543 34 H13 Z" fill="var(--ink)"/>
      </svg>
      <span>RESTORE STEEL SURFACES HOLOGRAM FREE</span>
    </div>

    <section class="steps">
      <div class="step"><div class="step__num">1</div><div class="step__label">PREWASH</div></div>
      <span class="step__divider">|</span>
      <div class="step step--highlight"><div class="step__num">2</div><div class="step__label">CLEAN</div></div>
      <span class="step__divider">|</span>
      <div class="step"><div class="step__num">3</div><div class="step__label">PROTECT</div></div>
      <span class="step__divider">|</span>
      <div class="step"><div class="step__num">4</div><div class="step__label">PRESERVE</div></div>
    </section>

    <section class="safety">
      <div class="safety__block safety__block--hazard">
        <svg class="hazard-symbol" viewBox="0 0 52 52" role="img" aria-label="Warning symbol">
          <path d="M26 3 L49 26 L26 49 L3 26 Z" fill="var(--white)" stroke="var(--hazard-red)" stroke-width="4" stroke-linejoin="round"/>
          <rect x="23.5" y="14" width="5" height="17" rx="1.5" fill="var(--ink)"/>
          <circle cx="26" cy="37" r="3" fill="var(--ink)"/>
        </svg>
        <div>
          <div class="safety__title">WARNING</div>
          <p>Causes serious eye irritation. Keep out of reach of children. If in eyes: rinse cautiously with water for several minutes.</p>
        </div>
      </div>
      <div class="safety__block">
        <div>
          <div class="safety__title">DIRECTIONS</div>
          <p>Spray evenly onto a clean, dry steel surface. Wipe with a microfibre cloth along the grain. Buff until streak free.</p>
        </div>
      </div>
    </section>

    <div class="website">
      <svg width="18" height="18" viewBox="0 0 18 18" aria-hidden="true">
        <g fill="none" stroke="var(--ink)" stroke-width="1.8">
          <circle cx="9" cy="9" r="7.5"/>
          <ellipse cx="9" cy="9" rx="3.2" ry="7.5"/>
          <line x1="1.5" y1="9" x2="16.5" y2="9"/>
        </g>
      </svg>
      WWW.KALMIRCOMPOUNDS.COM
    </div>
  </main>
</body>
</html>
```